Bref créative
The Quiet Fiddler
Notes on the Path Melodic
Rex Pembury
This is a revised e-book edition of a didactic memoir that has earned praise from major recording artists, symphonic musicians, and music-industry leaders. The book contains musical and social commentary; advice; interviews; memories of America, Europe, and the Middle East; and reference material.
Music
Drummers and other musicians, students, parents, baby boomers, and anyone else who enjoys musical stories, tips, and information.
The author is primarily a drum-set player and timpanist. Any image of a drum set should feature Stanmore drums and Vorkel cymbals (preferably from the 1960s); no other brands are acceptable. (Visit these companies' Web sites and oldstanmorekits.example for ideas.) Photos of 18th-century timpani (kettledrums) are equally appropriate. A photomontage will work, provided it is uncluttered and will reproduce well online (Tindral, eTomes, Cobb & Fairley, et al.).

```html
<!DOCTYPE html>
<html lang="en">
<head>
<meta charset="utf-8">
<title>The Quiet Fiddler – Cover Sizes</title>
<link rel="stylesheet" href="https://fonts.googleapis.com/css2?family=Arimo&family=Playfair+Display:wght@700&family=Libre+Baskerville:ital,wght@0,700;1,400&display=swap">
<style>
  :root {
    --page-bg: #ffffff;
    --label-ink: #1a1a1a;
    --cover-dark: #0d0b0c;
    --photo-deep: #16120f;
    --photo-mid: #3b2e25;
    --photo-warm: #6a5140;
    --title-orange: #d4561f;
    --title-edge: #3a1206;
    --subtitle-ink: #d9d2c6;
    --author-ink: #f2ede4;
    --rule-orange: #b8471a;
  }
  * { box-sizing: border-box; margin: 0; padding: 0; }
  html, body {
    width: 1200px; height: 593px; overflow: hidden;
    background: var(--page-bg);
  }
  .sheet { position: relative; width: 1200px; height: 593px; }

  .size-label {
    position: absolute;
    font-family: "Arimo", Arial, sans-serif;
    font-size: 19px;
    line-height: 22px;
    color: var(--label-ink);
    white-space: nowrap;
  }
  .label-cobb    { left: 43px;  top: 80px; }
  .label-tindral { left: 456px; top: 42px; }
  .label-etomes  { left: 850px; top: 32px; }

  .cover {
    position: absolute;
    overflow: hidden;
    background: var(--cover-dark);
    box-shadow: 0 0 0 1px #222;
  }
  .cover-photo {
    position: absolute; left: 0; top: 0; width: 100%; height: 72%;
    background:
      radial-gradient(ellipse at 55% 32%, var(--photo-warm) 0%, rgba(106,81,64,0) 45%),
      linear-gradient(180deg, var(--photo-mid) 0%, var(--photo-deep) 80%, var(--cover-dark) 100%);
  }
  .cover-type {
    position: absolute; left: 0; width: 100%;
    display: flex; flex-direction: column; align-items: center;
  }
  .cover-title {
    font-family: "Playfair Display", Georgia, serif;
    font-weight: 700;
    font-size: 46px;
    line-height: 56px;
    color: var(--title-orange);
    text-shadow: 1px 1px 0 var(--title-edge), -1px -1px 0 var(--title-edge);
    text-transform: uppercase;
    letter-spacing: 0.02em;
    align-self: flex-start;
    padding-left: 14%;
    white-space: nowrap;
  }
  .cover-title span { display: block; }
  .cover-subtitle {
    font-family: "Libre Baskerville", Georgia, serif;
    font-style: italic;
    font-size: 17px;
    line-height: 24px;
    color: var(--subtitle-ink);
    margin-top: 2px;
    white-space: nowrap;
  }
  .cover-rule { width: 100%; height: 2px; background: var(--rule-orange); }
  .cover-rule.upper { margin-top: 10px; }
  .cover-author {
    font-family: "Libre Baskerville", Georgia, serif;
    font-weight: 700;
    font-size: 19px;
    line-height: 39px;
    color: var(--author-ink);
    text-transform: uppercase;
    letter-spacing: 0.05em;
  }

  .cover-cobb    { left: 34px;  top: 134px; width: 346px; height: 421px; }
  .cover-tindral { left: 427px; top: 96px;  width: 352px; height: 470px; }
  .cover-etomes  { left: 816px; top: 67px;  width: 360px; height: 516px; }

  .cover-cobb .cover-type    { top: 140px; }
  .cover-tindral .cover-type { top: 188px; }
  .cover-etomes .cover-type  { top: 220px; }
</style>
</head>
<body>
<main class="sheet">
  <p class="size-label label-cobb">Cobb &amp; Fairley Cover: 600px x 730px</p>
  <p class="size-label label-tindral">Tindral Cover: 600px x 800px</p>
  <p class="size-label label-etomes">eTomes Cover: 600px x 860px</p>

  <article class="cover cover-cobb">
    <div class="cover-photo" role="img" aria-label="Photograph of a drummer playing a vintage drum set with cymbals, in warm low light"></div>
    <div class="cover-type">
      <h1 class="cover-title"><span>The</span><span>Quiet</span><span>Fiddler</span></h1>
      <p class="cover-subtitle">Notes on the Path Melodic</p>
      <div class="cover-rule upper"></div>
      <p class="cover-author">Rex Pembury</p>
      <div class="cover-rule"></div>
    </div>
  </article>

  <article class="cover cover-tindral">
    <div class="cover-photo" role="img" aria-label="Photograph of a drummer playing a vintage drum set with cymbals, in warm low light"></div>
    <div class="cover-type">
      <h1 class="cover-title"><span>The</span><span>Quiet</span><span>Fiddler</span></h1>
      <p class="cover-subtitle">Notes on the Path Melodic</p>
      <div class="cover-rule upper"></div>
      <p class="cover-author">Rex Pembury</p>
      <div class="cover-rule"></div>
    </div>
  </article>

  <article class="cover cover-etomes">
    <div class="cover-photo" role="img" aria-label="Photograph of a drummer playing a vintage drum set with cymbals, in warm low light"></div>
    <div class="cover-type">
      <h1 class="cover-title"><span>The</span><span>Quiet</span><span>Fiddler</span></h1>
      <p class="cover-subtitle">Notes on the Path Melodic</p>
      <div class="cover-rule upper"></div>
      <p class="cover-author">Rex Pembury</p>
      <div class="cover-rule"></div>
    </div>
  </article>
</main>
</body>
</html>
```